Tall Cedar Builders Business Card

I'm looking for a business card design for a start-up Handyman/Construction Company. The organization will double as a ministry to the homeless, hoping to create job opportunity and training to the homeless, providing a pathway back to being "homed". I'm looking for a simple to "seeming" simple design. Open to all thoughts.

Industry/Entity Type

Ministry

Requirements
Must have
• Logo (Attached), Name, Phone, Email and Address. Note - "*Registered and Insured".

```html
<!DOCTYPE html>
<html lang="en">
<head>
<meta charset="utf-8">
<title>Tall Cedar Builders Business Card</title>
<link href="https://fonts.googleapis.com/css2?family=Questrial&display=swap" rel="stylesheet">
<style>
  :root {
    --backdrop: #e4e4e1;
    --card-front: #f1f1f1;
    --card-back: #454545;
    --navy: #2b3553;
    --purple: #9b2f9f;
    --light-text: #f2f2f2;
    --soft-text: #d8d8d8;
  }
  * { margin: 0; padding: 0; box-sizing: border-box; }
  html, body {
    width: 1200px;
    height: 800px;
    overflow: hidden;
    background: var(--backdrop);
    font-family: "Questrial", "Century Gothic", sans-serif;
  }
  .canvas {
    position: relative;
    width: 1200px;
    height: 800px;
  }
  .card {
    position: absolute;
    box-shadow: 0 6px 16px rgba(0, 0, 0, 0.18);
  }
  .card-front {
    left: 168px;
    top: 280px;
    width: 560px;
    height: 280px;
    background: var(--card-front);
  }
  .brand {
    position: absolute;
    left: 132px;
    top: 120px;
    width: 302px;
  }
  .brand-line {
    display: flex;
    align-items: center;
    gap: 10px;
  }
  .brand-mark {
    width: 12px;
    height: 12px;
    background: var(--purple);
    flex: none;
  }
  .brand-name {
    color: var(--navy);
    font-size: 27px;
    line-height: 36px;
    letter-spacing: 0.5px;
    text-transform: uppercase;
    white-space: nowrap;
  }
  .brand-note {
    text-align: right;
    color: var(--navy);
    font-size: 11px;
    margin-top: 2px;
  }
  .card-back {
    left: 467px;
    top: 462px;
    width: 606px;
    height: 246px;
    background: var(--card-back);
    color: var(--light-text);
  }
  .person {
    position: absolute;
    top: 60px;
    left: 0;
    right: 0;
    text-align: center;
  }
  .person-name {
    font-size: 20px;
    letter-spacing: 0.5px;
    font-weight: 400;
    line-height: 24px;
  }
  .person-role {
    font-size: 11px;
    color: var(--purple);
    margin-top: 1px;
    margin-left: -40px;
  }
  .contact {
    position: absolute;
    top: 172px;
    left: 0;
    right: 0;
    text-align: center;
    font-size: 11.5px;
    color: var(--soft-text);
    line-height: 1.25;
  }
  .contact .label { color: var(--purple); }
  .contact-rule {
    position: absolute;
    left: 154px;
    width: 326px;
    top: 220px;
    height: 2px;
    background: var(--purple);
  }
</style>
</head>
<body>
  <main class="canvas">
    <section class="card card-front">
      <div class="brand">
        <div class="brand-line">
          <span class="brand-mark"></span>
          <span class="brand-name">Tall Cedar Builders</span>
        </div>
        <p class="brand-note">*Registered and Insured</p>
      </div>
    </section>

    <section class="card card-back">
      <div class="person">
        <h1 class="person-name">Marina DELACOURT</h1>
        <p class="person-role">Managing Partner</p>
      </div>
      <div class="contact">
        <p>4120 NW 18th Avenue, Tampa, FL 33604</p>
        <p><span class="label">T:</span> +1 813 555 0142 · <span class="label">E:</span> info@tallcedar.com</p>
      </div>
      <div class="contact-rule"></div>
    </section>
  </main>
</body>
</html>
```